Keystone Ward Security - Trade Show Booth 10x20

I need designs for an upcoming trade show booth. We want something sleek, simple that represents our brand well.

Target Market(s)

property Managers

```html
<!DOCTYPE html>
<html lang="en">
<head>
<meta charset="utf-8">
<title>Keystone Ward Security – Trade Show Booth</title>
<link rel="stylesheet" href="https://fonts.googleapis.com/css2?family=Montserrat:wght@500;700;800;900&display=swap">
<style>
  :root{
    --page:#ffffff;
    --charcoal:#26231f;
    --charcoal-deep:#1a1815;
    --charcoal-soft:#3a3631;
    --red:#e2432b;
    --red-dark:#b8311d;
    --white:#ffffff;
    --muted:#cfcac4;
  }
  *{box-sizing:border-box;margin:0;padding:0}
  html,body{width:776px;height:1200px;overflow:hidden;background:var(--page)}
  body{font-family:"Montserrat",Arial,sans-serif;color:var(--white);position:relative}

  /* Back wall banner */
  .banner{position:absolute;left:0;top:255px;width:776px;height:435px;background:var(--charcoal);overflow:hidden}
  .banner-shapes{position:absolute;inset:0}
  .headline{position:absolute;left:22px;top:16px;font-size:48px;font-weight:900;letter-spacing:-0.5px;line-height:1;white-space:nowrap}
  .tagline-band{position:absolute;left:0;top:86px;height:32px;width:300px;background:var(--red);
    display:flex;align-items:center;padding-left:22px;font-size:18px;font-weight:800;white-space:nowrap}
  .coverage{position:absolute;right:24px;top:95px;font-size:11.5px;font-weight:700;white-space:nowrap}

  .brand{position:absolute;left:50%;transform:translateX(-50%);text-align:center;display:flex;flex-direction:column;align-items:center}
  .brand-mark{width:28px;height:28px;background:var(--red);margin-bottom:10px}
  .brand-name{font-weight:800;color:var(--white);line-height:1.15;letter-spacing:1px;text-transform:uppercase;white-space:nowrap}
  .banner .brand{top:142px}
  .banner .brand-name{font-size:18px}

  .service-list{position:absolute;top:142px;list-style:none;display:flex;flex-direction:column;gap:12px}
  .service-list.left{left:24px}
  .service-list.right{left:535px}
  .service-list li{display:flex;align-items:center;gap:9px;font-size:12px;font-weight:700;white-space:nowrap}
  .service-list li small{font-size:8.5px;font-weight:700;margin-left:3px}
  .service-list svg{width:16px;height:16px;flex:none}

  .crew-photo{position:absolute;left:0;right:0;bottom:0;height:190px;
    background:linear-gradient(180deg,rgba(38,35,31,1) 0%,rgba(96,92,88,.85) 45%,rgba(62,58,54,1) 100%)}
  .web{position:absolute;left:0;right:0;text-align:center;font-size:12px;font-weight:600;color:var(--white)}
  .banner .web{top:262px}

  /* Counter front panel */
  .counter{position:absolute;left:213px;top:750px;width:350px;height:195px;background:var(--charcoal);overflow:hidden}
  .counter .brand{top:38px}
  .counter .brand-mark{width:22px;height:22px;margin-bottom:8px}
  .counter .brand-name{font-size:13px}
  .counter .web{top:128px;font-size:9px}
</style>
</head>
<body>

<section class="banner" aria-label="Back wall banner">
  <svg class="banner-shapes" viewBox="0 0 776 435" preserveAspectRatio="none" aria-hidden="true">
    <polygon points="280,122 496,122 496,250 388,295 280,250" fill="var(--charcoal-soft)"/>
  </svg>

  <div class="crew-photo" role="img" aria-label="Photo of uniformed security officers on patrol"></div>

  <svg class="banner-shapes" viewBox="0 0 776 435" preserveAspectRatio="none" aria-hidden="true">
    <polygon points="0,330 90,330 170,435 0,435" fill="var(--red)"/>
    <polygon points="0,370 60,370 110,435 0,435" fill="var(--red-dark)"/>
    <polygon points="776,330 686,330 606,435 776,435" fill="var(--red)"/>
    <polygon points="776,370 716,370 666,435 776,435" fill="var(--red-dark)"/>
  </svg>

  <h1 class="headline">Your Assets. Our Priority.</h1>
  <div class="tagline-band">Proactive Protection 24/7.</div>
  <p class="coverage">From Guards to Integrated Systems — All Covered.</p>

  <ul class="service-list left">
    <li><svg viewBox="0 0 20 20"><circle cx="10" cy="6" r="4" fill="var(--red)"/><path d="M3 18c0-4 3-6 7-6s7 2 7 6z" fill="var(--red)"/></svg>Security Guards</li>
    <li><svg viewBox="0 0 20 20"><path d="M2 13l2-5h12l2 5v3H2z" fill="var(--red)"/><circle cx="6" cy="16" r="2" fill="var(--charcoal)"/><circle cx="14" cy="16" r="2" fill="var(--charcoal)"/></svg>Mobile Patrol</li>
    <li><svg viewBox="0 0 20 20"><rect x="2" y="5" width="12" height="8" rx="1" fill="var(--red)"/><path d="M14 7l4-2v8l-4-2z" fill="var(--red)"/></svg>Integrated<small>Security Systems</small></li>
    <li><svg viewBox="0 0 20 20"><circle cx="6" cy="7" r="3" fill="var(--red)"/><circle cx="14" cy="7" r="3" fill="var(--red)"/><path d="M1 17c0-3 2-5 5-5s5 2 5 5zM9 17c0-3 2-5 5-5s5 2 5 5z" fill="var(--red)"/></svg>Event Staff</li>
  </ul>

  <div class="brand">
    <span class="brand-mark" aria-hidden="true"></span>
    <span class="brand-name">Keystone Ward<br>Security</span>
  </div>

  <ul class="service-list right">
    <li><svg viewBox="0 0 20 20"><path d="M10 2l8 15H2z" fill="var(--red)"/><rect x="9" y="7" width="2" height="5" fill="var(--charcoal)"/><rect x="9" y="13.5" width="2" height="2" fill="var(--charcoal)"/></svg>Emergency Response</li>
    <li><svg viewBox="0 0 20 20"><path d="M10 2l7 3v5c0 4-3 7-7 8-4-1-7-4-7-8V5z" fill="var(--red)"/></svg>Executive Protection</li>
    <li><svg viewBox="0 0 20 20"><path d="M10 2c1 4 6 6 6 11a6 6 0 01-12 0c0-3 2-4 3-6 1 2 2 2 3 2 0-2-1-4 0-7z" fill="var(--red)"/></svg>Fire Watch</li>
    <li><svg viewBox="0 0 20 20"><circle cx="8" cy="8" r="5" fill="none" stroke="var(--red)" stroke-width="2.5"/><path d="M12 12l5 5" stroke="var(--red)" stroke-width="3"/></svg>Private Investigations</li>
  </ul>

  <p class="web">www.keystonewardsec.com</p>
</section>

<section class="counter" aria-label="Counter front panel">
  <svg class="banner-shapes" viewBox="0 0 350 195" preserveAspectRatio="none" aria-hidden="true">
    <polygon points="110,20 240,20 240,105 175,130 110,105" fill="var(--charcoal-soft)"/>
    <polygon points="0,160 120,160 175,180 230,160 350,160 350,195 0,195" fill="var(--red)"/>
  </svg>
  <div class="brand">
    <span class="brand-mark" aria-hidden="true"></span>
    <span class="brand-name">Keystone Ward<br>Security</span>
  </div>
  <p class="web">www.keystonewardsec.com</p>
</section>

</body>
</html>
```